Reef Lantern Tropical Fish Startup Design

I need professional business cards and social media profiles for our tropical fish shop.

Target Market(s)

Tropical fish enthusiasts

Industry/Entity Type

Tropical Fish

Font styles to use
Sans Serif
Script
Other font styles liked:
• Comforta

Colors
0054AA
0677BA
7BADD7
CADEEF
E8F1F8
0094D4
00A9DD
6FCCEA
C7EBF8
E9F6FB
00AB8E
00BBA5
67D7C9
C6EFE9
E9F9F6

Requirements
Must have
• fish, oceanic colors
Nice to have
• Lines, boxes, anything that groups the title to stand out
Should not have
• Any punctuations

```html
<!DOCTYPE html>
<html lang="en">
<head>
<meta charset="utf-8">
<title>Reef Lantern Business Card</title>
<link rel="stylesheet" href="https://fonts.googleapis.com/css2?family=Montserrat:wght@800&family=Arimo:wght@400;700&display=swap">
<style>
  :root {
    --bg: #e9e9e8;
    --card-white: #f7f7f6;
    --panel-grey: #e3e3e3;
    --ghost-grey: #cfcfcf;
    --teal: #1aaa8c;
    --teal-deep: #149a7f;
    --teal-light: #4cbc9f;
    --blue: #1f58a0;
    --ink: #555555;
    --white: #ffffff;
  }
  html, body {
    margin: 0;
    padding: 0;
    width: 1200px;
    height: 801px;
    overflow: hidden;
    background: var(--bg);
  }
  .canvas {
    position: relative;
    width: 1200px;
    height: 801px;
  }
  .card {
    position: absolute;
    top: 245px;
    width: 540px;
    height: 310px;
    overflow: hidden;
    box-shadow: 0 10px 24px rgba(0,0,0,0.16);
  }
  /* front */
  .card-front {
    left: 45px;
    background: var(--card-white);
    font-family: "Arimo", Arial, sans-serif;
  }
  .front-panel {
    position: absolute;
    right: 0;
    top: 0;
    width: 240px;
    height: 290px;
    background: var(--panel-grey);
  }
  .front-ghost-name {
    position: absolute;
    right: -30px;
    top: 110px;
    font-family: "Montserrat", sans-serif;
    font-weight: 800;
    font-size: 84px;
    line-height: 1;
    color: var(--ghost-grey);
    white-space: nowrap;
    opacity: 0.8;
  }
  .front-address {
    position: absolute;
    right: 20px;
    top: 200px;
    text-align: right;
    font-size: 14px;
    line-height: 1.3;
    color: var(--ink);
  }
  .front-strip-teal {
    position: absolute;
    left: 0;
    bottom: 0;
    width: 300px;
    height: 20px;
    background: var(--teal);
  }
  .front-strip-blue {
    position: absolute;
    right: 0;
    bottom: 0;
    width: 240px;
    height: 20px;
    background: var(--blue);
  }
  .brand {
    position: absolute;
    left: 36px;
    top: 52px;
    display: flex;
    align-items: center;
    gap: 10px;
  }
  .brand-dot {
    width: 14px;
    height: 14px;
    border-radius: 50%;
    background: var(--teal);
  }
  .brand-name {
    font-family: "Montserrat", sans-serif;
    font-weight: 800;
    font-size: 34px;
    letter-spacing: 1px;
    color: var(--teal);
    white-space: nowrap;
  }
  .person {
    position: absolute;
    left: 40px;
    top: 130px;
  }
  .person-name {
    font-size: 19px;
    font-weight: 700;
    letter-spacing: 0.5px;
    color: var(--teal);
    text-transform: uppercase;
  }
  .person-role {
    font-size: 14px;
    color: var(--ink);
    margin-top: 2px;
  }
  .contacts {
    position: absolute;
    left: 40px;
    top: 190px;
    margin: 0;
    padding: 0;
    list-style: none;
  }
  .contact {
    display: flex;
    align-items: center;
    gap: 9px;
    font-size: 15px;
    color: var(--ink);
    height: 24px;
  }
  .contact svg {
    width: 14px;
    height: 14px;
    flex: none;
  }
  /* back */
  .card-back {
    left: 615px;
    background: var(--teal);
  }
  .back-shape {
    position: absolute;
    background: var(--teal-light);
    opacity: 0.55;
  }
  .back-shape-left {
    left: -40px;
    top: 40px;
    width: 210px;
    height: 300px;
    transform: skewX(-14deg);
  }
  .back-shape-right {
    right: -70px;
    top: -60px;
    width: 300px;
    height: 300px;
    border-radius: 50%;
  }
  .back-shape-shade {
    position: absolute;
    left: 160px;
    top: 0;
    width: 120px;
    height: 310px;
    background: var(--teal-deep);
    opacity: 0.5;
  }
  .back-brand {
    position: absolute;
    left: 0;
    right: 0;
    top: 126px;
    display: flex;
    justify-content: center;
    align-items: center;
    gap: 12px;
  }
  .back-brand .brand-dot {
    width: 18px;
    height: 18px;
    background: var(--white);
  }
  .back-brand .brand-name {
    font-size: 46px;
    color: var(--white);
  }
</style>
</head>
<body>
<main class="canvas">

  <section class="card card-front" aria-label="Business card front">
    <div class="front-panel"></div>
    <div class="front-ghost-name" aria-hidden="true">Reef Lantern</div>
    <div class="front-address">Your address<br>city, state, ZIP 0000</div>
    <div class="front-strip-teal"></div>
    <div class="front-strip-blue"></div>

    <div class="brand">
      <span class="brand-dot"></span>
      <span class="brand-name">Reef Lantern</span>
    </div>

    <div class="person">
      <div class="person-name">Dana Whitfield</div>
      <div class="person-role">Manager</div>
    </div>

    <ul class="contacts">
      <li class="contact">
        <svg viewBox="0 0 16 16" aria-hidden="true"><circle cx="8" cy="8" r="8" fill="#1aaa8c"/><path d="M5 4.5l1.6-.3.8 2-1 .7a5 5 0 0 0 2.7 2.7l.7-1 2 .8-.3 1.6c-3.6.3-6.8-2.9-6.5-6.5z" fill="#fff"/></svg>
        555-014-2100
      </li>
      <li class="contact">
        <svg viewBox="0 0 16 16" aria-hidden="true"><rect x="1" y="3" width="14" height="10" rx="1" fill="#1aaa8c"/><path d="M1.5 3.5L8 9l6.5-5.5" stroke="#fff" stroke-width="1.3" fill="none"/></svg>
        hello@reeflantern.com
      </li>
      <li class="contact">
        <svg viewBox="0 0 16 16" aria-hidden="true"><circle cx="8" cy="8" r="7.5" fill="#1aaa8c"/><g stroke="#fff" stroke-width="1" fill="none"><circle cx="8" cy="8" r="5"/><ellipse cx="8" cy="8" rx="2.2" ry="5"/><path d="M3 8h10"/></g></svg>
        www.reeflantern.shop
      </li>
    </ul>
  </section>

  <section class="card card-back" aria-label="Business card back">
    <div class="back-shape back-shape-left"></div>
    <div class="back-shape back-shape-right"></div>
    <div class="back-shape-shade"></div>
    <div class="back-brand">
      <span class="brand-dot"></span>
      <span class="brand-name">Reef Lantern</span>
    </div>
  </section>

</main>
</body>
</html>
```